Q&Q Electric Skateboards Website - California Beach - Psychedelic - Graffiti Style

CARTVANE WEBSITE: Opening a online Q&Q Electric Skateboards shop. We'll ultimately sell Electric Skateboards, Scooters and Bikes. I opened a Cartvane account and even purchased a domain. But, after 3 weeks of trying, I realize, my skills are inadequate. I'd love to have a cool website that links to Parcelbay / Bidlot / Snapreel / Friendwall etc.I'd really like to emphasize that we're a coastal california company, with offices in Hermosa Beach, Venice Beach, and Santa Cruz. I like the colorful, psychedelic color patterns, with graffiti letteringIdeally, I'd like to have a couple pages1. Landing Page with a menu for2. Electric Skateboards (a) Street skateboards (small wheels) (4 offerings) (b) Commuter / offroad skateboards (2 offerings)2. Scooter (1 offering)3. Bikes (1 offering)4. Parts5. Link to an apparel site6. Blog / Safety Tips / Maintenance7. Our Company?I've attached a couple pix and logos etc. I suspect you'll see I have an idea of what I want to do, but my execution isn't so good...I love to have some input and for somebody to help me get a site running! THANK YOU!!

Target Market(s)

Not entirely sure. My gut is 20 - 40 year olds, largely male. Commuters and Students

Industry/Entity Type

Sporting Good

Contact Information for Business Card

I really like the Graffiti Style lettering, you'll see I did them poorly on the attachment - originally, I thought that some bright, graffiti lettering of Q&Q Electric Skateboards or Q&Q Skateboards on the front. Bright logo on the back with all of the information below
Marco Penhale
(213) 555-0147
mpenhale@qqboardworks.example
www.qqboardworks.example

Coding

Coded - Design and coding required

Number of Pages Required

1 page

Font styles to use
Other font styles liked:
• Comic Sans MS

Colors
fbed22
e34197
ec1f27
0292cd
6b449b

Requirements
Must have
• Please See "Final Design Selection" (one of the last files on my upload list) to get a sense of the custom decks we're having printed. These are the first couple, but, I think you'll get a sense
• Also, please look at the "Logo - First Attempt " powerpoint file. That's my attempt at graffiti style lettering (one of the last files on the list of uploads)
• Finally, please look at the Delia Markovetz photo (first file on upload list). It's a public access photo. But, I love the picture

```html
<!DOCTYPE html>
<html lang="en">
<head>
<meta charset="utf-8">
<title>Q&amp;Q Electric Skateboards</title>
<link href="https://fonts.googleapis.com/css2?family=Roboto:wght@400;500;700;900&family=Roboto+Condensed:wght@700&display=swap" rel="stylesheet">
<style>
:root{
  --purple:#6b449b;
  --pink:#e34197;
  --blue:#0292cd;
  --yellow:#fbed22;
  --ink:#222;
  --muted:#555;
  --line:#e3e3e3;
  --soft:#f7f7f8;
  --dark:#1c1c1c;
}
*{box-sizing:border-box;margin:0;padding:0}
html,body{width:1200px;height:3719px;overflow:hidden}
body{position:relative;font-family:"Roboto",Arial,sans-serif;color:var(--ink);background:#fff}
.abs{position:absolute}
.topbar{left:0;top:0;width:1200px;height:40px;background:var(--purple);color:#fff;font-size:11px}
.topbar .links{left:160px;top:13px;word-spacing:2px}
.topbar .links span{margin-right:16px}
.topbar .support{left:420px;top:13px;display:flex;gap:6px;align-items:center}
.social{display:flex;gap:9px}
.social i{display:block;width:26px;height:26px;border-radius:50%;border:1.5px solid #fff}
.topbar .social{left:908px;top:7px}
.header{left:0;top:40px;width:1200px;height:102px;background:#fff}
.logo{left:160px;top:14px;display:flex;align-items:center;gap:10px;font-size:26px;font-weight:900;color:var(--purple)}
.logo b{display:block;width:38px;height:38px;border-radius:50%;background:var(--pink)}
.search{left:543px;top:28px;width:356px;height:44px;border:2px solid var(--purple);border-radius:22px}
.search .btn{position:absolute;right:6px;top:6px;width:28px;height:28px;border-radius:50%;background:var(--purple)}
.cart{left:910px;top:28px;width:130px;height:44px;border:2px solid var(--purple);border-radius:22px;font-size:12px;display:flex;align-items:center;justify-content:center;gap:8px;color:var(--ink)}
.hero{left:0;top:142px;width:1200px;height:508px;background:linear-gradient(180deg,#8a8e96 0%,#b3a99b 45%,#6d7a45 80%,#4e5b2e 100%)}
.nav{left:160px;top:142px;width:880px;height:50px;background:var(--pink);display:flex;align-items:center;font-size:11px;font-weight:500;color:#fff}
.nav span{margin-left:46px;margin-right:22px}
.nav .choose{position:absolute;left:650px;top:9px;width:215px;height:32px;border:1px solid rgba(255,255,255,.8);padding:9px 12px;font-size:10px}
.nav .choose:after{content:"";position:absolute;right:12px;top:12px;border:4px solid transparent;border-top-color:#fff}
.hero-title{left:0;top:355px;width:1200px;text-align:center;color:#fff;font-family:"Roboto Condensed",sans-serif}
.hero-title h1{font-size:50px;line-height:1;letter-spacing:1px}
.hero-title h2{font-size:34px;line-height:1.2;margin-top:8px}
.arrow{width:38px;height:38px;border-radius:50%;background:rgba(0,0,0,.35);top:367px}
.arrow svg{display:block;margin:12px auto}
.promo-l{left:0;top:650px;width:593px;height:158px;background:var(--blue);color:#fff}
.promo-r{left:593px;top:650px;width:607px;height:158px;background:var(--pink);color:#fff}
.promo-l h3{position:absolute;left:160px;top:22px;width:400px;font-family:"Roboto Condensed",sans-serif;font-size:21px;line-height:1.3}
.promo-l p{position:absolute;left:160px;top:100px;font-size:16px;letter-spacing:.3px}
.promo-r h3{position:absolute;left:34px;top:24px;font-family:"Roboto Condensed",sans-serif;font-size:23px}
.promo-r p{position:absolute;left:34px;top:58px;width:440px;font-size:11px;line-height:1.45}
.ghost{display:inline-block;border:2px solid #fff;color:#fff;font-size:10.5px;font-weight:500;padding:9px 12px}
.promo-r .ghost{position:absolute;left:34px;top:108px}
.section{left:0;width:1200px;background:var(--soft)}
.sec-head{position:absolute;left:0;width:1200px;text-align:center}
.sec-head h2{font-family:"Roboto Condensed",sans-serif;font-size:30px;color:var(--ink)}
.sec-head hr{width:44px;border:0;border-top:2px solid var(--pink);margin:8px auto 14px}
.sec-head p{width:580px;margin:0 auto;font-size:11px;line-height:1.55;color:var(--ink)}
.cards{position:absolute;left:160px;width:880px;display:flex;gap:11px}
.card{width:212px;height:360px;background:#fff;border:1px solid var(--line);text-align:center}
.card .pic{height:160px;margin:8px;background:linear-gradient(180deg,#fff,#eef0f3)}
.card .pic.photo{margin:0;height:160px;background:linear-gradient(135deg,#1e2a4a,#5a3fb0 55%,#2a2f3a)}
.card h4{font-size:13px;font-weight:500;margin-top:20px}
.card .price{font-size:26px;font-weight:700;color:var(--blue);margin-top:4px}
.card p{font-size:10.5px;line-height:1.4;color:var(--muted);width:150px;margin:6px auto 0}
.stars{font-size:13px;letter-spacing:2px;margin-top:6px;color:#222}
.stars em{font-style:normal;color:#bbb}
.btns{display:flex;justify-content:center;gap:10px;margin-top:14px}
.btns span{width:86px;height:32px;line-height:32px;font-size:9.5px;font-weight:500;color:#fff}
.btns .add{background:var(--pink)}
.btns .view{background:var(--purple)}
.pager{position:absolute;left:573px;display:flex;gap:6px}
.pager i{display:block;width:24px;height:22px;background:var(--pink)}
.pager svg{display:block;margin:6px auto}
.feature-photo{background:linear-gradient(135deg,#3a3f47,#6e7680 50%,#2c3038)}
.feature{color:#fff}
.feature h3{position:absolute;font-family:"Roboto Condensed",sans-serif;font-size:27px}
.feature p{position:absolute;font-size:11px;line-height:1.65;text-align:justify}
.quote{position:absolute;top:2945px;width:262px;height:190px;border:1px solid #ddd;background:#fff;padding:18px 16px;font-size:11px;line-height:1.55;color:var(--muted)}
.person{position:absolute;top:3118px;display:flex;align-items:center;gap:12px}
.person .ava{width:54px;height:54px;border-radius:50%;background:linear-gradient(135deg,#c9b7a7,#8c7565)}
.person b{display:block;font-size:13px;font-weight:700}
.person small{font-size:10px;color:var(--muted)}
.guarantee{left:0;top:3224px;width:1200px;height:144px;background:var(--blue);color:#fff}
.guarantee .box{position:absolute;left:220px;top:16px;width:740px;height:112px;border:2px solid #fff}
.guarantee h3{position:absolute;left:16px;top:22px;font-family:"Roboto Condensed",sans-serif;font-size:23px}
.guarantee p{position:absolute;left:16px;top:60px;font-size:13px}
.badge{position:absolute;left:898px;top:22px;width:90px;height:90px;border-radius:50%;background:#2b2b2b;border:4px solid #c7c7c7}
.footer{left:0;top:3368px;width:1200px;height:351px;background:var(--dark);color:#fff}
.footer h5{position:absolute;top:58px;font-size:13px;font-weight:700;letter-spacing:.5px}
.footer h5:after{content:"";display:block;width:40px;border-top:1px solid #fff;margin-top:8px}
.footer .about{position:absolute;left:160px;top:100px;width:220px;font-size:11px;line-height:1.6}
.footer .social{position:absolute;left:160px;top:212px}
.footer .social i{width:30px;height:30px;background:#fff;border:0}
.contact{position:absolute;left:517px;top:100px;font-size:11px}
.contact div{display:flex;align-items:center;gap:10px;height:29px}
.field{position:absolute;left:757px;width:270px;height:34px;border:1px solid #666;font-size:11px;padding:10px 12px;color:#ccc}
.submit{position:absolute;left:757px;top:202px;width:90px;height:28px;background:#fff;color:#111;border-radius:14px;font-size:11px;font-weight:700;text-align:center;line-height:28px}
.copy{position:absolute;left:160px;top:315px;font-size:10.5px;color:#ddd}
</style>
</head>
<body>

<div class="abs topbar">
  <div class="abs links"><span>Check Out</span><span>Register Or Sign In</span></div>
  <div class="abs support">
    <svg width="12" height="12" viewBox="0 0 24 24"><path fill="#fff" d="M6.6 10.8a15 15 0 0 0 6.6 6.6l2.2-2.2c.3-.3.7-.4 1-.2 1.1.4 2.3.6 3.6.6.6 0 1 .4 1 1V20c0 .6-.4 1-1 1A17 17 0 0 1 3 4c0-.6.4-1 1-1h3.5c.6 0 1 .4 1 1 0 1.3.2 2.5.6 3.6.1.3 0 .7-.2 1z"/></svg>
    <span>Free Call Support : +(012) 555 0199</span>
  </div>
  <div class="abs social"><i></i><i></i><i></i><i></i></div>
</div>

<div class="abs header">
  <div class="abs logo"><b></b>Q&amp;Q Skateboards</div>
  <div class="abs search"><span class="btn"><svg width="28" height="28" viewBox="0 0 28 28"><circle cx="13" cy="13" r="5" fill="none" stroke="#fff" stroke-width="2"/><path d="M17 17l4 4" stroke="#fff" stroke-width="2"/></svg></span></div>
  <div class="abs cart">
    <svg width="14" height="12" viewBox="0 0 24 20"><path d="M1 1h4l3 12h12l3-9H7" fill="none" stroke="#333" stroke-width="2"/><circle cx="9" cy="17" r="2" fill="#333"/><circle cx="19" cy="17" r="2" fill="#333"/></svg>
    <span>$ 100</span>
    <svg width="8" height="6" viewBox="0 0 8 6"><path d="M0 0h8L4 6z" fill="#333"/></svg>
  </div>
</div>

<div class="abs hero" role="img" aria-label="Rider in helmet and pads on an electric skateboard, sunlit grass behind"></div>
<div class="abs nav">
  <span>HOME</span><span>ABOUT US</span><span>SHOP</span><span>PRODUCTS</span><span>CONTACT US</span>
  <div class="choose">Choose a Product</div>
</div>
<div class="abs hero-title"><h1>4WHEEL</h1><h2>ELECTRIC SKATEBOARD</h2></div>
<div class="abs arrow" style="left:24px"><svg width="14" height="14" viewBox="0 0 14 14"><path d="M9 2L4 7l5 5" fill="none" stroke="#fff" stroke-width="2"/></svg></div>
<div class="abs arrow" style="left:1128px"><svg width="14" height="14" viewBox="0 0 14 14"><path d="M5 2l5 5-5 5" fill="none" stroke="#fff" stroke-width="2"/></svg></div>

<div class="abs promo-l">
  <h3>WE PROVIDE BEST PRODUCTS THAT YOU DESERVES !</h3>
  <p>FREE SHIPPING ON ORDERS OVER $300</p>
</div>
<div class="abs promo-r">
  <h3>NEW ARRIVALS 2018</h3>
  <p>Lorem Ipsum is simply dummy text of the printing and typesetting industry. Lorem Ipsum has been the industry's standard dummy text ever since</p>
  <span class="ghost">READ MOORE</span>
</div>

<section class="abs section" style="top:808px;height:635px">
  <div class="sec-head" style="top:50px">
    <h2>OUR PRODUCT</h2><hr>
    <p>Lorum ipsilum than two centuries of craftsmanship and a perpetual commitment to perfection. There is no mystery about a Suit Me, simply more than two centuries of craftsmanship.</p>
  </div>
  <div class="cards" style="top:182px">
    <div class="card"><div class="pic" role="img" aria-label="Top view of a black electric skateboard deck"></div><h4>LOREM IPSUM IS SIMPLY</h4><div class="price">$350</div><p>Lorem Ipsum is simply dummy text of printing dummy text of</p><div class="stars">★★★★★</div><div class="btns"><span class="add">ADD TO CART</span><span class="view">VIEW DETAILS</span></div></div>
    <div class="card"><div class="pic" role="img" aria-label="Off-road electric skateboard with large tyres"></div><h4>LOREM IPSUM IS SIMPLY</h4><div class="price">$450</div><p>Lorem Ipsum is simply dummy text of printing dummy text of</p><div class="stars">★★★<em>★★</em></div><div class="btns"><span class="add">ADD TO CART</span><span class="view">VIEW DETAILS</span></div></div>
    <div class="card"><div class="pic" role="img" aria-label="Patterned electric skateboard deck, top view"></div><h4>LOREM IPSUM IS SIMPLY</h4><div class="price">$250</div><p>Lorem Ipsum is simply dummy text of printing dummy text of</p><div class="stars">★★<em>★★★</em></div><div class="btns"><span class="add">ADD TO CART</span><span class="view">VIEW DETAILS</span></div></div>
    <div class="card"><div class="pic" role="img" aria-label="All-terrain electric skateboard, side view"></div><h4>LOREM IPSUM IS SIMPLY</h4><div class="price">$550</div><p>Lorem Ipsum is simply dummy text of printing dummy text of</p><div class="stars">★<em>★★★★</em></div><div class="btns"><span class="add">ADD TO CART</span><span class="view">VIEW DETAILS</span></div></div>
  </div>
  <div class="pager" style="top:572px"><i><svg width="8" height="10" viewBox="0 0 8 10"><path d="M6 1L2 5l4 4" fill="none" stroke="#fff" stroke-width="1.5"/></svg></i><i><svg width="8" height="10" viewBox="0 0 8 10"><path d="M2 1l4 4-4 4" fill="none" stroke="#fff" stroke-width="1.5"/></svg></i></div>
</section>

<div class="abs feature-photo" style="left:0;top:1443px;width:613px;height:347px" role="img" aria-label="Rider crouching on a lit off-road electric skateboard in an underpass at night"></div>
<div class="abs feature" style="left:613px;top:1443px;width:587px;height:347px;background:var(--pink)">
  <h3 style="left:39px;top:54px">4WHEEL</h3>
  <p style="left:39px;top:108px;width:505px">Lorum Ipsilum than two centuries of craftsmanship and a perpetual commitment to perfection. There is no mystery about a Suit Me, simply more than two centuries of craftsmanship and a perpetual commitment to perfection.Lorum Ipsilum than two centuries of craftsmanship and a perpetual commitment to perfection. There is no mystery</p>
  <span class="ghost" style="position:absolute;left:39px;top:242px">READ MOORE</span>
</div>
<div class="abs feature" style="left:0;top:1790px;width:613px;height:345px;background:var(--blue)">
  <h3 style="left:160px;top:50px">LOREM IPSUM IS SIMPLY</h3>
  <p style="left:160px;top:104px;width:405px">Lorum Ipsilum than two centuries of craftsmanship and a perpetual commitment to perfection. There is no mystery about a Suit Me, simply more than two centuries of craftsmanship and a perpetual commitment to perfection.Lorum Ipsilum than two centuries of craftsmanship and a perpetual commitment to perfection. There is no mystery</p>
  <span class="ghost" style="position:absolute;left:160px;top:244px">READ MOORE</span>
</div>
<div class="abs feature-photo" style="left:613px;top:1790px;width:587px;height:345px" role="img" aria-label="Rider adjusting a glowing off-road electric skateboard on a plaza"></div>

<section class="abs section" style="top:2135px;height:625px">
  <div class="sec-head" style="top:48px">
    <h2>BEST SELLER</h2><hr>
    <p>Lorum ipsilum than two centuries of craftsmanship and a perpetual commitment to perfection. There is no mystery about a Suit Me, simply more than two centuries of craftsmanship.</p>
  </div>
  <div class="cards" style="top:183px">
    <div class="card"><div class="pic photo" role="img" aria-label="Electric skateboard with blue underglow"></div><h4>LOREM IPSUM IS SIMPLY</h4><div class="price">$350</div><p>Lorem Ipsum is simply dummy text of printing dummy text of</p><div class="stars">★★★★★</div><div class="btns"><span class="add">ADD TO CART</span><span class="view">VIEW DETAILS</span></div></div>
    <div class="card"><div class="pic photo" role="img" aria-label="Electric skateboard lit in purple at night"></div><h4>LOREM IPSUM IS SIMPLY</h4><div class="price">$450</div><p>Lorem Ipsum is simply dummy text of printing dummy text of</p><div class="stars">★★★<em>★★</em></div><div class="btns"><span class="add">ADD TO CART</span><span class="view">VIEW DETAILS</span></div></div>
    <div class="card"><div class="pic photo" style="background:linear-gradient(135deg,#6f7780,#c6ccd2 55%,#4a5058)" role="img" aria-label="Off-road electric skateboard on pavement"></div><h4>LOREM IPSUM IS SIMPLY</h4><div class="price">$250</div><p>Lorem Ipsum is simply dummy text of printing dummy text of</p><div class="stars">★★<em>★★★</em></div><div class="btns"><span class="add">ADD TO CART</span><span class="view">VIEW DETAILS</span></div></div>
    <div class="card"><div class="pic photo" role="img" aria-label="Electric skateboard with glowing wheels"></div><h4>LOREM IPSUM IS SIMPLY</h4><div class="price">$550</div><p>Lorem Ipsum is simply dummy text of printing dummy text of</p><div class="stars">★<em>★★★★</em></div><div class="btns"><span class="add">ADD TO CART</span><span class="view">VIEW DETAILS</span></div></div>
  </div>
  <div class="pager" style="top:572px"><i><svg width="8" height="10" viewBox="0 0 8 10"><path d="M6 1L2 5l4 4" fill="none" stroke="#fff" stroke-width="1.5"/></svg></i><i><svg width="8" height="10" viewBox="0 0 8 10"><path d="M2 1l4 4-4 4" fill="none" stroke="#fff" stroke-width="1.5"/></svg></i></div>
</section>

<section class="abs" style="left:0;top:2760px;width:1200px;height:464px;background:#fff">
  <div class="sec-head" style="top:52px">
    <h2>TESTIMONIALS</h2><hr>
    <p>Lorum ipsilum than two centuries of craftsmanship and a perpetual commitment to perfection. There is no mystery about a Suit Me, simply more than two centuries of craftsmanship.</p>
  </div>
</section>
<div class="quote" style="left:180px">Lorem Ipsum is simply dummy text of the printing and typesetting industry. Lorem Ipsum has been the industry's standard dummy text ever since the. Lorem Ipsum is simply dummy text of the printing and.</div>
<div class="quote" style="left:467px">Lorem Ipsum is simply dummy text of the printing and typesetting industry. Lorem Ipsum has been the industry's standard dummy text ever since the. Lorem Ipsum is simply dummy text of the printing and.</div>
<div class="quote" style="left:764px">Lorem Ipsum is simply dummy text of the printing and typesetting industry. Lorem Ipsum has been the industry's standard dummy text ever since the. Lorem Ipsum is simply dummy text of the printing and.</div>
<div class="person" style="left:190px"><div class="ava" role="img" aria-label="Customer portrait"></div><div><b>RAVI OKONEDO</b><small>LOREM IPSUM IS SIMPLY</small></div></div>
<div class="person" style="left:477px"><div class="ava" role="img" aria-label="Customer portrait"></div><div><b>LENA BRACKWATER</b><small>LOREM IPSUM IS SIMPLY</small></div></div>
<div class="person" style="left:774px"><div class="ava" role="img" aria-label="Customer portrait"></div><div><b>OTTO FAIRWEATHER</b><small>LOREM IPSUM IS SIMPLY</small></div></div>

<div class="abs guarantee">
  <div class="box">
    <h3>15 DAY MONEY BACK GUARANTEE!</h3>
    <p>If your return your order anytime withing 30 days, we'll send your money back. No Questions Asked.</p>
    <div class="badge" role="img" aria-label="Guarantee seal"></div>
  </div>
</div>

<footer class="abs footer">
  <h5 style="left:160px">ABOUT US</h5>
  <p class="about">Lorem ipsum dolor sit amet, consectetur adipiscing elit. Aenean vel interdum tellus. Suspendisse leo libero, sollicitudin interdum tellus.</p>
  <div class="social"><i></i><i></i><i></i><i></i></div>
  <h5 style="left:517px">CONTACT INFO</h5>
  <div class="contact">
    <div><svg width="11" height="13" viewBox="0 0 12 16"><path d="M6 0a6 6 0 0 1 6 6c0 4-6 10-6 10S0 10 0 6a6 6 0 0 1 6-6z" fill="#fff"/><circle cx="6" cy="6" r="2" fill="#1c1c1c"/></svg>14 Pier Lane – Hermosa Beach</div>
    <div><svg width="11" height="11" viewBox="0 0 24 24"><path fill="#fff" d="M6.6 10.8a15 15 0 0 0 6.6 6.6l2.2-2.2c.3-.3.7-.4 1-.2 1.1.4 2.3.6 3.6.6.6 0 1 .4 1 1V20c0 .6-.4 1-1 1A17 17 0 0 1 3 4c0-.6.4-1 1-1h3.5c.6 0 1 .4 1 1 0 1.3.2 2.5.6 3.6.1.3 0 .7-.2 1z"/></svg>+ (012) 555 0199</div>
    <div><svg width="12" height="9" viewBox="0 0 12 9"><rect width="12" height="9" fill="#fff"/><path d="M0 0l6 5 6-5" fill="none" stroke="#1c1c1c"/></svg>hello@qqboardworks.example</div>
    <div><svg width="12" height="12" viewBox="0 0 12 12"><circle cx="6" cy="6" r="5" fill="none" stroke="#fff" stroke-width="1.3"/><path d="M1 6h10M6 1c-3 3-3 7 0 10M6 1c3 3 3 7 0 10" fill="none" stroke="#fff"/></svg>www.qqboardworks.example</div>
  </div>
  <h5 style="left:757px">NEWS LETTER</h5>
  <div class="field" style="top:100px">Name...</div>
  <div class="field" style="top:148px">E-Mail...</div>
  <div class="submit">SUBMIT</div>
  <p class="copy">© 2018 Q&amp;Q Electric Skateboards . All Rights Reserved.</p>
</footer>

</body>
</html>
```